M&A Advisory firm needs elegant and powerful letterhead

We need a powerful but elegant letterhead to engage with the international financial industry.

Target Market(s)

New York and International Financial Industry

Industry/Entity Type

Finance

Font styles to use
Other font styles liked:
• Poppins

Requirements
Must have
• 482 W 71st Street 14th Floor New York, NY 10157 O: +1 (212) 555 0147 F: +1 (212) 555 0182

```html
<!DOCTYPE html>
<html lang="en">
<head>
<meta charset="utf-8">
<title>Meridane Letterhead</title>
<link href="https://fonts.googleapis.com/css2?family=Poppins:wght@400;500&family=Arimo:wght@400&display=swap" rel="stylesheet">
<style>
  :root {
    --paper: #f6f4f4;
    --brand-blue: #1a4f93;
    --ink: #3a3a3a;
    --ink-soft: #4a4a4a;
    --ink-dark: #1f1f1f;
    --signature-tone: #2b2f3a;
  }
  * { margin: 0; padding: 0; box-sizing: border-box; }
  html, body { width: 935px; height: 1200px; overflow: hidden; background: var(--paper); }
  .letterhead {
    position: relative;
    width: 935px;
    height: 1200px;
    background: var(--paper);
    font-family: "Arimo", Arial, sans-serif;
    color: var(--ink);
  }
  .brand {
    position: absolute;
    left: 92px;
    top: 112px;
    display: flex;
    align-items: center;
    gap: 12px;
  }
  .brand-dot {
    width: 26px; height: 26px;
    border-radius: 50%;
    background: var(--brand-blue);
  }
  .brand-name {
    font-family: "Poppins", sans-serif;
    font-weight: 400;
    font-size: 38px;
    letter-spacing: 1px;
    color: var(--brand-blue);
    line-height: 1;
  }
  .contact {
    position: absolute;
    left: 696px;
    top: 100px;
    font-family: "Poppins", sans-serif;
    font-size: 13px;
    line-height: 16px;
    color: var(--ink-dark);
  }
  .contact-address { margin-bottom: 10px; }
  .contact-line { display: flex; align-items: center; gap: 7px; }
  .contact-line svg { width: 12px; height: 12px; fill: var(--brand-blue); }
  .greeting {
    position: absolute;
    left: 93px;
    top: 300px;
    font-size: 25px;
    color: var(--ink-soft);
  }
  .body-copy {
    position: absolute;
    left: 93px;
    top: 378px;
    width: 752px;
    font-size: 14.6px;
    line-height: 20.4px;
    text-align: justify;
    color: var(--ink);
  }
  .body-copy p { margin-bottom: 20.4px; }
  .closing {
    position: absolute;
    left: 93px;
    top: 828px;
    font-size: 14.6px;
    color: var(--ink);
  }
  .signature {
    position: absolute;
    left: 90px;
    top: 862px;
    width: 122px;
    height: 44px;
    background: linear-gradient(90deg, rgba(43,47,58,0.12), rgba(43,47,58,0.22), rgba(43,47,58,0.1));
    border-radius: 4px;
  }
  .signer {
    position: absolute;
    left: 97px;
    top: 926px;
  }
  .signer-name { font-size: 19px; color: var(--ink-soft); line-height: 24px; }
  .signer-title { font-size: 15px; color: var(--ink-soft); line-height: 22px; }
</style>
</head>
<body>
<main class="letterhead">
  <header>
    <div class="brand">
      <span class="brand-dot"></span>
      <span class="brand-name">MERIDANE</span>
    </div>
    <address class="contact" style="font-style:normal">
      <div class="contact-address">482 W 71st Street<br>14th Floor New York<br>NY 10157</div>
      <div class="contact-line">
        <svg viewBox="0 0 24 24" aria-hidden="true"><path d="M6.6 10.8a15.1 15.1 0 0 0 6.6 6.6l2.2-2.2a1 1 0 0 1 1-.25 11.4 11.4 0 0 0 3.6.6 1 1 0 0 1 1 1V20a1 1 0 0 1-1 1A17 17 0 0 1 3 4a1 1 0 0 1 1-1h3.5a1 1 0 0 1 1 1c0 1.25.2 2.45.6 3.6a1 1 0 0 1-.25 1z"/></svg>
        <span>+1 (212) 555 0147</span>
      </div>
      <div class="contact-line">
        <svg viewBox="0 0 24 24" aria-hidden="true"><path d="M6 2h10l2 2v5H6zM3 10h18a1 1 0 0 1 1 1v8a1 1 0 0 1-1 1H3a1 1 0 0 1-1-1v-8a1 1 0 0 1 1-1zm3 4v2h12v-2z"/></svg>
        <span>+1 (212) 555 0182</span>
      </div>
    </address>
  </header>

  <h1 class="greeting" style="font-weight:400">Dear Mr. Harlow,</h1>

  <section class="body-copy">
    <p>Lorem ipsum dolor sit amet, consectetur adipiscing elit. Donec orci purus, luctus vitae dignissim eu, iaculis sed purus. Vivamus faucibus, ipsum nec aliquet viverra, leo mauris condimentum ligula, sit amet sagittis enim ligula quis arcu. Nam egestas tortor id nisi porttitor mattis. In tortor ante, ultricies in suscipit a, tempus non massa. Vivamus et auctor mi. Fusce vel massa nulla. Phasellus nec eros mauris, et scelerisque orci.</p>
    <p>Donec malesuada orci vitae nulla accumsan porta a id massa. Quisque accumsan iaculis magna sit amet fringilla. Maecenas consequat, magna eget tincidunt semper, odio nibh rutrum mi, id feugiat ante nisi eu risus. Vestibulum nunc orci, rhoncus a placerat in, ultricies in mi. Cras mattis varius eros, vel fringilla nisi suscipit eget. Quisque scelerisque sagittis nulla at porttitor.</p>
    <p>Sed id augue vitae urna euismod commodo aliquet a quam. Pellentesque arcu velit, cursus et malesuada ut, consequat et diam. Nullam erat sem, rhoncus id ullamcorper vitae, rhoncus et arcu. In ultricies ultricies nulla, ut rutrum nisi iaculis at. Donec eu magna a metus ornare faucibus. Fusce aliquet faucibus ultricies. Morbi semper, est id tincidunt gravida, sem arcu adipiscing lacus, ac bibendum nulla leo eu purus. Quisque nec diam sed risus consectetur a ccumsan quis quis nibh. Vestibulum id purus lorem.</p>
    <p>It is a long established fact that a reader will be distracted by the readable content of a page when looking at its layout. The point of using Lorem Ipsum is that it has a more-or-less normal distribution of letters, as opposed to using 'Content here, content here', making it look like readable English. Many desktop publishing packages</p>
  </section>

  <p class="closing">Sincerely,</p>
  <div class="signature" role="img" aria-label="Handwritten signature of Daniel Harlow"></div>
  <div class="signer">
    <div class="signer-name">Daniel Harlow</div>
    <div class="signer-title">CEO/ Founder</div>
  </div>
</main>
</body>
</html>
```